Shopify Website for Health & Beauty

The user must be available to answer questions quickly if there's an issue. Good communication skills require.

*These products are unisex for men & women*
www.valdoru.com

Website we like to model
https://www.lumbrivex-usa.com/
https://www.hollowmere.com/
https://www.zintock.com/

Pages:
Home, about us, contact us, affiliate, search, blog

Need to redesign my current website valdoru.com
We need a high converting website
Custom banner
Social media setup
Graphics design
Lifestyle images
Create a new Site Icon/Favicon
Custom popups
Web content
Klayivo setup for flows and custom newsletters
Create a Custom 404 Page
Set SEO Titles and Meta Descriptions
Optimize Your Site's Performance
*Set Up Your Homepage
Add metadata to all pages
Use schema markup whenever possible
Check for technical SEO errors

```html
<!DOCTYPE html>
<html lang="en">
<head>
<meta charset="utf-8">
<title>Valdoru — Advanced Hair Care</title>
<link href="https://fonts.googleapis.com/css2?family=Oswald:wght@400;500;600&family=Montserrat:wght@300;400;500;600;700&family=Playfair+Display&display=swap" rel="stylesheet">
<style>
:root{
  --yellow:#f8c400;
  --yellow-soft:#f9cc1f;
  --ink:#1d1d1d;
  --nav:#222325;
  --footer:#202124;
  --text:#333;
  --muted:#777;
  --line:#e6e6e6;
  --sale:#e0262d;
  --green:#4caf50;
  --star:#f5b400;
}
*{box-sizing:border-box;margin:0;padding:0}
html,body{width:1200px;height:4152px;overflow:hidden}
body{font-family:"Montserrat",sans-serif;color:var(--text);background:#fff;position:relative}
a{color:inherit;text-decoration:none}

.topbar{height:37px;background:var(--yellow);display:flex;align-items:center;justify-content:space-between;padding:0 100px;font-size:13px;color:#1d1d1d;white-space:nowrap}
.topbar strong{font-weight:600}
.topbar .ship{display:flex;align-items:center;gap:8px}

.nav{height:65px;background:var(--nav);display:flex;align-items:center;padding:0 100px;color:#fff;white-space:nowrap}
.brand{font-family:"Montserrat",sans-serif;font-weight:600;font-size:28px;width:220px;flex:none}
.menu{display:flex;gap:26px;margin-left:102px;font-size:13px;font-weight:600;flex:none}
.tools{margin-left:auto;display:flex;gap:24px;font-size:14px;align-items:center;flex:none}
.tools span{display:flex;align-items:center;gap:6px}

.hero{height:577px;position:relative;background:linear-gradient(100deg,#7f93ae 0%,#5f7899 45%,#4a6283 100%);overflow:hidden}
.hero .photo{position:absolute;inset:0}
.hero .copy{position:absolute;left:98px;top:140px;color:#fff;white-space:nowrap}
.hero h1{font-family:"Oswald",sans-serif;font-weight:500;font-size:54px;line-height:1.25;letter-spacing:.5px}
.hero h1 em{font-style:italic;color:var(--yellow)}
.hero p{font-size:31px;font-weight:500;margin-top:6px}
.btn{display:inline-block;background:var(--yellow);color:#1d1d1d;font-weight:600;font-size:16px;border-radius:22px;padding:11px 28px;white-space:nowrap}
.hero .btn{margin-top:26px;padding:10px 28px;font-size:16px}
.hero .arrow{position:absolute;left:58px;top:290px}
.bottle{position:absolute;border-radius:26px 26px 18px 18px;background:linear-gradient(90deg,#1c1c1e,#3a3a3d 40%,#1a1a1b)}

.section-title{font-family:"Oswald",sans-serif;font-weight:500;font-size:46px;text-align:center;color:#111}

.categories{position:absolute;top:760px;left:0;width:1200px}
.cat-grid{display:grid;grid-template-columns:repeat(4,241px);gap:13px;margin:28px 0 0 100px}
.cat{height:307px;border:1px solid #eee;box-shadow:0 1px 4px rgba(0,0,0,.06);display:flex;flex-direction:column;align-items:center}
.cat .img{width:170px;height:212px;margin-top:22px;border-radius:8px}
.cat h3{font-family:"Oswald",sans-serif;font-weight:500;font-size:22px;margin-top:28px;color:#222}

.sellers{position:absolute;left:0;width:1200px}
.grid{display:grid;grid-template-columns:repeat(4,242px);column-gap:13px;row-gap:16px;margin:26px 0 0 100px}
.card{height:407px;border:1px solid #eee;box-shadow:0 1px 4px rgba(0,0,0,.06);position:relative;text-align:center}
.sale{position:absolute;left:10px;top:10px;background:var(--sale);color:#fff;font-size:13px;font-weight:600;padding:2px 12px;letter-spacing:.5px}
.heart{position:absolute;right:10px;top:8px}
.card .img{position:absolute;left:50%;transform:translateX(-50%);top:18px;width:110px;height:250px;border-radius:10px}
.card .img.wide{width:165px;height:150px;top:80px;border-radius:14px}
.card .img.jar{width:140px;height:140px;top:90px;border-radius:12px}
.card .img.slim{width:60px}
.card h4{position:absolute;top:272px;width:100%;font-family:"Oswald",sans-serif;font-weight:500;font-size:14px;color:#222;white-space:nowrap}
.price{position:absolute;top:298px;width:100%;display:flex;justify-content:center;align-items:center;gap:6px}
.price b{font-size:17px;font-weight:600;color:#222}
.stars{color:var(--star);font-size:11px;letter-spacing:-.5px}
.price small{font-size:10px;color:#555}
.stock{position:absolute;top:325px;width:100%;font-size:11px;color:#555;display:flex;justify-content:center;align-items:center;gap:5px}
.dot{width:11px;height:11px;border-radius:50%;background:var(--green);display:inline-flex}
.buy{position:absolute;top:356px;width:100%;display:flex;justify-content:center;gap:12px}
.qty{width:46px;height:29px;border:1px solid #ddd;font-size:11px;color:#888;display:flex;align-items:center;justify-content:center}
.add{width:118px;height:29px;background:var(--yellow);font-size:11px;font-weight:700;display:flex;align-items:center;justify-content:center;color:#111}

.promos{position:absolute;top:2403px;left:106px;display:grid;grid-template-columns:480px 480px;gap:20px}
.promo{text-align:center}
.promo .img{height:344px}
.promo h3{font-family:"Playfair Display",serif;font-weight:400;font-size:32px;margin-top:20px;color:#222;white-space:nowrap}
.promo p{font-size:15px;line-height:1.5;margin:6px auto 0;width:460px;color:#333}
.promo .btn{border-radius:0;padding:9px 22px;font-size:15px;font-weight:500;margin-top:14px}

.features{position:absolute;top:3677px;left:0;width:1200px;height:93px;display:grid;grid-template-columns:300px 300px 300px 300px;background:var(--yellow)}
.feature{display:flex;align-items:center;gap:10px;padding-left:55px;padding-right:10px;color:#222}
.feature:nth-child(even){background:var(--yellow-soft)}
.feature b{display:block;font-size:14px;font-weight:700;white-space:nowrap}
.feature span{font-size:11.5px;line-height:1.25;display:block}

.footer{position:absolute;top:3770px;left:0;width:1200px;height:382px;background:var(--footer);color:#fff}
.footer h5{font-size:16px;font-weight:600;margin-bottom:16px}
.col{position:absolute;top:61px}
.col ul{list-style:none;font-size:13px;line-height:29px}
.col p{font-size:11.5px;line-height:22px}
.contact{font-size:13px;margin-top:10px;line-height:28px;display:flex;flex-direction:column}
.subscribe{width:207px;height:36px;border-radius:18px;background:#fff;color:#888;font-size:12px;display:flex;align-items:center;justify-content:space-between;padding:0 4px 0 12px;margin-top:12px}
.subscribe i{width:28px;height:28px;border-radius:50%;background:var(--yellow);display:flex;align-items:center;justify-content:center}
.social{display:flex;gap:9px;margin-top:20px}
.social span{width:42px;height:42px;border:2px solid #fff;border-radius:50%;display:flex;align-items:center;justify-content:center}
.social span::after{content:"";width:8px;height:8px;background:#fff;border-radius:50%}
.copy-row{position:absolute;top:340px;left:119px;right:100px;display:flex;justify-content:space-between;font-size:12px}
.pay{display:flex;gap:20px;font-size:12px;font-weight:600}
</style>
</head>
<body>

<div class="topbar">
  <strong>COVID - 19 UPDATE</strong>
  <div class="ship">
    <svg width="22" height="16" viewBox="0 0 22 16" fill="none" stroke="#1d1d1d" stroke-width="1.4"><rect x="1" y="2" width="12" height="9"/><path d="M13 5h4l3 3v3h-7"/><circle cx="5" cy="13" r="2" fill="#f8c400"/><circle cx="16" cy="13" r="2" fill="#f8c400"/></svg>
    Free shipping on orders over $50
  </div>
  <strong>Need Help? 888-888-8888</strong>
</div>

<nav class="nav">
  <div class="brand">Valdoru</div>
  <div class="menu"><a>HOME</a><a>ABOUT US</a><a>CONTACT US</a><a>AFFILIATE</a><a>BLOG</a></div>
  <div class="tools">
    <span><svg width="17" height="17" viewBox="0 0 17 17" fill="none" stroke="#fff" stroke-width="1.6"><circle cx="7" cy="7" r="5.5"/><path d="M11 11l5 5"/></svg>Search</span>
    <span><svg width="12" height="13" viewBox="0 0 12 13" fill="#fff"><circle cx="6" cy="3.5" r="3.2"/><path d="M0 13c0-4 3-6 6-6s6 2 6 6z"/></svg>Login ⌄</span>
    <span><svg width="16" height="15" viewBox="0 0 16 15" fill="#fff"><path d="M0 1h3l2 8h9l2-6H5"/><circle cx="6" cy="13" r="1.5"/><circle cx="13" cy="13" r="1.5"/></svg>Cart</span>
  </div>
</nav>

<header class="hero">
  <div class="photo" role="img" aria-label="Lifestyle photo of two dark shampoo bottles with a feather and glass beads on a blue-grey backdrop"></div>
  <div class="bottle" style="left:737px;top:148px;width:170px;height:415px"></div>
  <div class="bottle" style="left:875px;top:92px;width:185px;height:460px"></div>
  <svg class="arrow" width="24" height="40" viewBox="0 0 24 40" fill="none" stroke="#fff" stroke-width="2"><path d="M20 2L4 20l16 18"/></svg>
  <div class="copy">
    <h1>VALDORU BLOWOUT SALE<br>UPTO <em>20% OFF</em></h1>
    <p>on select valdoru's brand items</p>
    <a class="btn">SHOP NOW</a>
  </div>
</header>

<section class="categories">
  <h2 class="section-title">SHOP BY CATEGORY</h2>
  <div class="cat-grid">
    <div class="cat"><div class="img" role="img" aria-label="Dark shampoo bottle with leaf line drawing" style="background:linear-gradient(90deg,#f4f4f2,#2a2a2c 30%,#3a3a3c 70%,#f4f4f2)"></div><h3>Skin Care</h3></div>
    <div class="cat"><div class="img" role="img" aria-label="White serum pump bottle with leaf line drawing" style="background:linear-gradient(90deg,#fafafa,#dcdcdc 40%,#f0f0f0 60%,#fafafa)"></div><h3>Hair Care</h3></div>
    <div class="cat"><div class="img" role="img" aria-label="Dark treatment masque tube" style="background:linear-gradient(90deg,#f6f6f4,#2b2b2d 20%,#3b3b3d 80%,#f6f6f4)"></div><h3>Category</h3></div>
    <div class="cat"><div class="img" role="img" aria-label="Clear serum pump bottle with yellow label" style="background:linear-gradient(90deg,#fafafa,#e4e4e4 40%,#f2e2a0 55%,#fafafa)"></div><h3>Category</h3></div>
  </div>
</section>

<section class="sellers" style="top:1315px">
  <h2 class="section-title">TOP SELLERS</h2>
  <div class="grid">
    <div class="card"><span class="sale">SALE</span><svg class="heart" width="22" height="20" viewBox="0 0 22 20" fill="none" stroke="#555" stroke-width="1.4"><path d="M11 18S2 12 2 6.5A4.5 4.5 0 0 1 11 4a4.5 4.5 0 0 1 9 2.5C20 12 11 18 11 18z"/></svg><div class="img" role="img" aria-label="Dark strengthening shampoo bottle" style="background:linear-gradient(90deg,#1f1f21,#404043 50%,#1f1f21)"></div><h4>DELUXE RENEWAL SERUM (4 OZ)</h4><div class="price"><b>$23.40</b><span class="stars">★★★★★</span><small>(5.0)</small></div><div class="stock"><i class="dot"></i>In Stock</div><div class="buy"><span class="qty">Qty</span><span class="add">ADD TO CART</span></div></div>
    <div class="card"><span class="sale">SALE</span><svg class="heart" width="22" height="20" viewBox="0 0 22 20" fill="none" stroke="#555" stroke-width="1.4"><path d="M11 18S2 12 2 6.5A4.5 4.5 0 0 1 11 4a4.5 4.5 0 0 1 9 2.5C20 12 11 18 11 18z"/></svg><div class="img slim" role="img" aria-label="Clear serum pump bottle" style="background:linear-gradient(180deg,#d8d8d8,#f2f2f2 40%,#f0d860 60%,#eee)"></div><h4>DELUXE RENEWAL SERUM (4 OZ)</h4><div class="price"><b>$23.40</b><span class="stars">★★★★★</span><small>(5.0)</small></div><div class="stock"><i class="dot"></i>In Stock</div><div class="buy"><span class="qty">Qty</span><span class="add">ADD TO CART</span></div></div>
    <div class="card"><span class="sale">SALE</span><svg class="heart" width="22" height="20" viewBox="0 0 22 20" fill="none" stroke="#555" stroke-width="1.4"><path d="M11 18S2 12 2 6.5A4.5 4.5 0 0 1 11 4a4.5 4.5 0 0 1 9 2.5C20 12 11 18 11 18z"/></svg><div class="img" role="img" aria-label="Dark treatment tube" style="width:130px;height:220px;top:40px;background:linear-gradient(90deg,#1f1f21,#404043 50%,#1f1f21)"></div><h4>DELUXE RENEWAL SERUM (4 OZ)</h4><div class="price"><b>$23.40</b><span class="stars">★★★★★</span><small>(5.0)</small></div><div class="stock"><i class="dot"></i>In Stock</div><div class="buy"><span class="qty">Qty</span><span class="add">ADD TO CART</span></div></div>
    <div class="card"><span class="sale">SALE</span><svg class="heart" width="22" height="20" viewBox="0 0 22 20" fill="none" stroke="#555" stroke-width="1.4"><path d="M11 18S2 12 2 6.5A4.5 4.5 0 0 1 11 4a4.5 4.5 0 0 1 9 2.5C20 12 11 18 11 18z"/></svg><div class="img wide" role="img" aria-label="White skincare pads jar" style="background:linear-gradient(180deg,#f3f3f3,#e6e9ee 60%,#f5f5f5)"></div><h4>DELUXE RENEWAL SERUM (4 OZ)</h4><div class="price"><b>$23.40</b><span class="stars">★★★★★</span><small>(5.0)</small></div><div class="stock"><i class="dot"></i>In Stock</div><div class="buy"><span class="qty">Qty</span><span class="add">ADD TO CART</span></div></div>

    <div class="card"><span class="sale">SALE</span><svg class="heart" width="22" height="20" viewBox="0 0 22 20" fill="none" stroke="#555" stroke-width="1.4"><path d="M11 18S2 12 2 6.5A4.5 4.5 0 0 1 11 4a4.5 4.5 0 0 1 9 2.5C20 12 11 18 11 18z"/></svg><div class="img" role="img" aria-label="White cleanser tube" style="width:80px;background:linear-gradient(90deg,#ececec,#fafafa 50%,#e8e8e8)"></div><h4>DELUXE RENEWAL SERUM (4 OZ)</h4><div class="price"><b>$23.40</b><span class="stars">★★★★★</span><small>(5.0)</small></div><div class="stock"><i class="dot"></i>In Stock</div><div class="buy"><span class="qty">Qty</span><span class="add">ADD TO CART</span></div></div>
    <div class="card"><span class="sale">SALE</span><svg class="heart" width="22" height="20" viewBox="0 0 22 20" fill="none" stroke="#555" stroke-width="1.4"><path d="M11 18S2 12 2 6.5A4.5 4.5 0 0 1 11 4a4.5 4.5 0 0 1 9 2.5C20 12 11 18 11 18z"/></svg><div class="img jar" role="img" aria-label="Dark hair pomade jar" style="background:linear-gradient(180deg,#111,#2a2a2c 60%,#111)"></div><h4>DELUXE RENEWAL SERUM (4 OZ)</h4><div class="price"><b>$23.40</b><span class="stars">★★★★★</span><small>(5.0)</small></div><div class="stock"><i class="dot"></i>In Stock</div><div class="buy"><span class="qty">Qty</span><span class="add">ADD TO CART</span></div></div>
    <div class="card"><span class="sale">SALE</span><svg class="heart" width="22" height="20" viewBox="0 0 22 20" fill="none" stroke="#555" stroke-width="1.4"><path d="M11 18S2 12 2 6.5A4.5 4.5 0 0 1 11 4a4.5 4.5 0 0 1 9 2.5C20 12 11 18 11 18z"/></svg><div class="img slim" role="img" aria-label="White brightening serum bottle" style="background:linear-gradient(180deg,#ddd,#f5f5f5 40%,#eee)"></div><h4>DELUXE RENEWAL SERUM (4 OZ)</h4><div class="price"><b>$23.40</b><span class="stars">★★★★★</span><small>(5.0)</small></div><div class="stock"><i class="dot"></i>In Stock</div><div class="buy"><span class="qty">Qty</span><span class="add">ADD TO CART</span></div></div>
    <div class="card"><span class="sale">SALE</span><svg class="heart" width="22" height="20" viewBox="0 0 22 20" fill="none" stroke="#555" stroke-width="1.4"><path d="M11 18S2 12 2 6.5A4.5 4.5 0 0 1 11 4a4.5 4.5 0 0 1 9 2.5C20 12 11 18 11 18z"/></svg><div class="img" role="img" aria-label="Dark strengthening shampoo bottle" style="background:linear-gradient(90deg,#1f1f21,#404043 50%,#1f1f21)"></div><h4>DELUXE RENEWAL SERUM (4 OZ)</h4><div class="price"><b>$23.40</b><span class="stars">★★★★★</span><small>(5.0)</small></div><div class="stock"><i class="dot"></i>In Stock</div><div class="buy"><span class="qty">Qty</span><span class="add">ADD TO CART</span></div></div>
  </div>
</section>

<section class="promos">
  <div class="promo">
    <div class="img" role="img" aria-label="Serum bottles and a jar on stone pedestals with palm-leaf shadows on a peach wall" style="background:linear-gradient(160deg,#c99a78,#b8805e 55%,#9c6a4c)"></div>
    <h3>Bundle Up &amp; Save 10%</h3>
    <p>Lorem ipsum dolor sit amet, consectetur adipiscing elit, sed do eiusmod tempor incididunt ut labore et dolore</p>
    <a class="btn">SHOP ALL SETS</a>
  </div>
  <div class="promo">
    <div class="img" role="img" aria-label="Lifestyle photo of a woman relaxing beside two dark shampoo bottles" style="background:linear-gradient(110deg,#7a6a55,#c7b8a0 45%,#d8d2c6 65%,#2c2c2e 80%)"></div>
    <h3>Best Hair Care for Thicker Hair</h3>
    <p>Lorem ipsum dolor sit amet, consectetur adipiscing elit, sed do eiusmod tempor incididunt ut labore et dolore</p>
    <a class="btn">SHOP THE DENSIFYING COLLECTION</a>
  </div>
</section>

<section class="sellers" style="top:3087px">
  <h2 class="section-title">TOP SELLERS</h2>
  <div class="grid">
    <div class="card"><span class="sale">SALE</span><svg class="heart" width="22" height="20" viewBox="0 0 22 20" fill="none" stroke="#555" stroke-width="1.4"><path d="M11 18S2 12 2 6.5A4.5 4.5 0 0 1 11 4a4.5 4.5 0 0 1 9 2.5C20 12 11 18 11 18z"/></svg><div class="img slim" role="img" aria-label="White brightening serum bottle" style="background:linear-gradient(180deg,#ddd,#f5f5f5 40%,#eee)"></div><h4>DELUXE RENEWAL SERUM (4 OZ)</h4><div class="price"><b>$23.40</b><span class="stars">★★★★★</span><small>(5.0)</small></div><div class="stock"><i class="dot"></i>In Stock</div><div class="buy"><span class="qty">Qty</span><span class="add">ADD TO CART</span></div></div>
    <div class="card"><span class="sale">SALE</span><svg class="heart" width="22" height="20" viewBox="0 0 22 20" fill="none" stroke="#555" stroke-width="1.4"><path d="M11 18S2 12 2 6.5A4.5 4.5 0 0 1 11 4a4.5 4.5 0 0 1 9 2.5C20 12 11 18 11 18z"/></svg><div class="img jar" role="img" aria-label="Dark hair pomade jar" style="background:linear-gradient(180deg,#111,#2a2a2c 60%,#111)"></div><h4>DELUXE RENEWAL SERUM (4 OZ)</h4><div class="price"><b>$23.40</b><span class="stars">★★★★★</span><small>(5.0)</small></div><div class="stock"><i class="dot"></i>In Stock</div><div class="buy"><span class="qty">Qty</span><span class="add">ADD TO CART</span></div></div>
    <div class="card"><span class="sale">SALE</span><svg class="heart" width="22" height="20" viewBox="0 0 22 20" fill="none" stroke="#555" stroke-width="1.4"><path d="M11 18S2 12 2 6.5A4.5 4.5 0 0 1 11 4a4.5 4.5 0 0 1 9 2.5C20 12 11 18 11 18z"/></svg><div class="img" role="img" aria-label="White cleanser tube" style="width:80px;background:linear-gradient(90deg,#ececec,#fafafa 50%,#e8e8e8)"></div><h4>DELUXE RENEWAL SERUM (4 OZ)</h4><div class="price"><b>$23.40</b><span class="stars">★★★★★</span><small>(5.0)</small></div><div class="stock"><i class="dot"></i>In Stock</div><div class="buy"><span class="qty">Qty</span><span class="add">ADD TO CART</span></div></div>
    <div class="card"><span class="sale">SALE</span><svg class="heart" width="22" height="20" viewBox="0 0 22 20" fill="none" stroke="#555" stroke-width="1.4"><path d="M11 18S2 12 2 6.5A4.5 4.5 0 0 1 11 4a4.5 4.5 0 0 1 9 2.5C20 12 11 18 11 18z"/></svg><div class="img" role="img" aria-label="Dark strengthening shampoo bottle" style="background:linear-gradient(90deg,#1f1f21,#404043 50%,#1f1f21)"></div><h4>DELUXE RENEWAL SERUM (4 OZ)</h4><div class="price"><b>$23.40</b><span class="stars">★★★★★</span><small>(5.0)</small></div><div class="stock"><i class="dot"></i>In Stock</div><div class="buy"><span class="qty">Qty</span><span class="add">ADD TO CART</span></div></div>
  </div>
</section>

<section class="features">
  <div class="feature"><svg width="36" height="26" viewBox="0 0 36 26" fill="none" stroke="#222" stroke-width="1.5"><rect x="2" y="4" width="20" height="14"/><path d="M22 9h7l5 5v4H22"/><circle cx="9" cy="21" r="3" fill="#f8c400"/><circle cx="28" cy="21" r="3" fill="#f8c400"/></svg><div><b>FAST SHIPPING</b><span>Deliveries throughout wide</span></div></div>
  <div class="feature"><svg width="30" height="30" viewBox="0 0 30 30" fill="none" stroke="#222" stroke-width="1.6"><path d="M5 17v-3a10 10 0 0 1 20 0v3"/><rect x="3" y="16" width="5" height="8" rx="2"/><rect x="22" y="16" width="5" height="8" rx="2"/><path d="M25 24c0 3-4 4-8 4"/></svg><div><b>SUPPORT 24/7</b><span>You will speak with one of our courteous representatives in 20 minutes or less.</span></div></div>
  <div class="feature"><svg width="34" height="34" viewBox="0 0 34 34" fill="none" stroke="#222" stroke-width="1.5"><rect x="4" y="6" width="20" height="24"/><path d="M8 12h12M8 17h12M8 22h8"/><circle cx="26" cy="24" r="6" fill="#f8c400"/><path d="M23 24l2 2 4-4"/></svg><div><b>MONEY BACK GUARANTEE</b><span>Guaranteed, of quality and in accordance with the law</span></div></div>
  <div class="feature"><svg width="36" height="28" viewBox="0 0 36 28" fill="none" stroke="#222" stroke-width="1.5"><rect x="2" y="4" width="28" height="18" rx="2"/><path d="M2 10h28M6 17h8"/><path d="M28 14l6 2v4c0 4-3 6-6 7-3-1-6-3-6-7v-4z" fill="#f8c400"/></svg><div><b>SECURE PAYMNETS</b><span>Your safety is our priority.<br>All payments are 100% secure.</span></div></div>
</section>

<footer class="footer">
  <div class="col" style="left:119px"><h5>QUICK LINKS</h5><ul><li>Search</li><li>Become a Seller</li><li>Contact Us</li><li>Refund Policy</li><li>Shipping Policy</li><li>Privacy Policy</li><li>Terms of Service</li></ul></div>
  <div class="col" style="left:310px"><h5>MAIN MENU</h5><ul><li>&nbsp;Home</li><li>About Us</li><li>Shop</li><li>Blog</li><li>Contact &amp; FAQ</li><li>Press &amp; Awards</li></ul></div>
  <div class="col" style="left:500px;width:340px"><h5>VALDORU</h5><p>Valdoru is a family owned and operated company that was born in 2019. We wanted to provide a healthy lifestyle for everyone, from haircare to skincare to vitamins.</p>
    <div class="contact"><span>✉&nbsp; info@valdoru.com</span><span>✆&nbsp; +888 888 8888</span></div></div>
  <div class="col" style="left:881px;width:230px"><h5>NEWS &amp; UPDATES</h5><p style="font-size:13px;line-height:28px">Sign up to get the latest on sales, new releases and more …</p>
    <div class="subscribe">Enter you email<i><svg width="14" height="14" viewBox="0 0 14 14" fill="#222"><path d="M13 1L1 6l5 2 2 5z"/></svg></i></div>
    <div class="social"><span aria-label="Social link"></span><span aria-label="Social link"></span><span aria-label="Social link"></span><span aria-label="Social link"></span></div></div>
  <div class="copy-row"><span>Copyright © 2021 Valdoru. All Rights Reserved.</span>
    <div class="pay"><span>Cardova</span><span>Meridan</span><span>Amplex</span><span>PayLune</span><span>Orbpay</span></div></div>
</footer>

</body>
</html>
```